Business Card Design

I am a florist specialising in weddings. I would like a very modern however elegant and simple design. My arrangement designs can be quite rustic with a vintage feel, so if you are able to reflect this in the card that would be great.
Updates

Thank you everyone for your submissions. I have found some further words for inspiration. I am looking for something more earthy and artisan looking. If possible I would like to use 100% recycled paper - the type that even looks rustic and recycled. I may even opt to use a small logo to emphasis the fact that they are made from recycled paper. I know this is quite different to my original brief but I wasn't quite sure what to expect from your designs. Also, with the logo, I give permission for it to be cropped to remove the 'Floral Designer' text. Please contact me if you need any further assistance. Many thanks Lisette Petal and Thistle Studio

I would prefer not to have any photgraphs & not too much pink. Thank you!

Industry/Entity Type

Florist

Contact Information for Business Card

Lisette Varko
Floral Designer
0417 365 820
lisette@petalthistlestudio.com.au
petalthistlestudio.com.au

Requirements
Must have
• My logo

```html
<!DOCTYPE html>
<html lang="en">
<head>
<meta charset="utf-8">
<title>Petal and Thistle Studio – Business Cards</title>
<link rel="stylesheet" href="https://fonts.googleapis.com/css2?family=Arvo:wght@400;700&family=Open+Sans:wght@400;600&display=swap">
<style>
  :root {
    --bg: #e8e3db;
    --card: #f3ece1;
    --card-light: #f8f3eb;
    --card-edge: #e9dfcf;
    --wine: #5e3440;
    --wine-dark: #4a2832;
    --sage: #a9a282;
    --ink: #2a2422;
    --grey: #5c5450;
    --bloom-area: #ebe4d6;
  }
  * { margin: 0; padding: 0; box-sizing: border-box; }
  html, body { width: 1200px; height: 1024px; overflow: hidden; }
  body {
    background: var(--bg);
    font-family: "Open Sans", Arial, sans-serif;
    position: relative;
  }
  .card {
    position: absolute;
    left: 250px;
    width: 700px;
    height: 400px;
    background: var(--card);
    box-shadow: 0 6px 18px rgba(0,0,0,0.14);
    overflow: hidden;
  }
  .card--front { top: 80px; }
  .card--back {
    top: 544px;
    background: radial-gradient(ellipse at 45% 40%, var(--card-light) 0%, var(--card) 60%, var(--card-edge) 100%);
  }
  .card__art { position: absolute; inset: 0; width: 100%; height: 100%; }

  .brand {
    position: absolute;
    display: flex;
    align-items: center;
    gap: 12px;
    font-family: "Arvo", Georgia, serif;
    font-weight: 400;
    color: var(--ink);
    white-space: nowrap;
  }
  .brand__dot {
    border-radius: 50%;
    background: var(--wine);
    flex: none;
  }
  .card--front .brand { left: 190px; top: 58px; font-size: 22px; }
  .card--front .brand__dot { width: 14px; height: 14px; }
  .card--back .brand {
    left: 0; right: 0; top: 0; bottom: 0;
    justify-content: center;
    font-size: 40px;
  }
  .card--back .brand__dot { width: 26px; height: 26px; }

  .holder { position: absolute; left: 44px; top: 200px; }
  .holder__name {
    font-family: "Arvo", Georgia, serif;
    font-weight: 700;
    font-size: 28px;
    color: var(--ink);
    letter-spacing: 0.2px;
  }
  .holder__role {
    margin-top: 8px;
    font-size: 17px;
    color: var(--wine);
  }
  .contact {
    position: absolute;
    left: 52px;
    top: 284px;
    list-style: none;
    font-size: 14px;
    color: var(--grey);
  }
  .contact__item {
    display: flex;
    align-items: center;
    gap: 16px;
    height: 30px;
  }
  .contact__icon { width: 16px; height: 16px; flex: none; }
</style>
</head>
<body>

<section class="card card--front" aria-label="Business card front">
  <svg class="card__art" viewBox="0 0 700 400" preserveAspectRatio="none">
    <path class="wave wave--sage" fill="var(--sage)"
          d="M300 400 C420 385 450 265 500 140 C540 50 580 0 625 0 L700 0 L700 400 Z"/>
    <path class="wave wave--gap" fill="var(--card)"
          d="M312 400 C430 385 462 268 512 146 C552 58 592 10 700 5 L700 400 Z"/>
    <path class="wave wave--wine" fill="var(--wine)"
          d="M326 400 C442 384 476 272 526 152 C566 64 606 18 700 14 L700 400 Z"/>
    <path class="wave wave--wine-shade" fill="var(--wine-dark)" opacity="0.35"
          d="M420 400 C520 370 560 280 610 180 C640 120 670 90 700 80 L700 400 Z"/>
    <circle class="bloom" cx="598" cy="82" r="68" fill="var(--bloom-area)"
            role="img" aria-label="Image of a white gerbera daisy"/>
  </svg>

  <div class="brand"><span class="brand__dot"></span><span class="brand__name">Petal and Thistle Studio</span></div>

  <div class="holder">
    <p class="holder__name">Lisette Varko</p>
    <p class="holder__role">Floral Designer</p>
  </div>

  <ul class="contact">
    <li class="contact__item">
      <svg class="contact__icon" viewBox="0 0 16 16"><path fill="var(--wine)" d="M4 1 L6.5 4 L5 6 C6 8.5 7.5 10 10 11 L12 9.5 L15 12 L13 15 C7 15 1 9 1 3 Z"/></svg>
      <span>0417 365 820</span>
    </li>
    <li class="contact__item">
      <svg class="contact__icon" viewBox="0 0 16 16"><circle cx="8" cy="8" r="8" fill="var(--wine)"/><rect x="3.5" y="5" width="9" height="6" fill="none" stroke="#fff" stroke-width="1.2"/><path d="M3.5 5 L8 8.5 L12.5 5" fill="none" stroke="#fff" stroke-width="1.2"/></svg>
      <span>lisette@petalthistlestudio.com.au</span>
    </li>
    <li class="contact__item">
      <svg class="contact__icon" viewBox="0 0 16 16"><circle cx="8" cy="8" r="8" fill="var(--wine)"/><circle cx="8" cy="8" r="5" fill="none" stroke="#fff" stroke-width="1.1"/><ellipse cx="8" cy="8" rx="2.2" ry="5" fill="none" stroke="#fff" stroke-width="1.1"/><path d="M3 8 H13" stroke="#fff" stroke-width="1.1"/></svg>
      <span>www.petalthistlestudio.com.au</span>
    </li>
  </ul>
</section>

<section class="card card--back" aria-label="Business card back">
  <div class="brand"><span class="brand__dot"></span><span class="brand__name">Petal and Thistle Studio</span></div>
</section>

</body>
</html>
```